Brasko Construction Business Card

I need a business card design for my company.
We are a construction/machinery company.
I would like to see my logo on the front of the card and my details on the other side
I would like the card to be black or dark grey in colour,with my logo as i send it or modified with a lighter blue colour
I would like to see the design kept fairly simple,but eye catching at the same time
Industry/Entity Type
Business
Contact Information for Business Card
Name
Phone Number
Address
Email
Colors
00a990
1b1b1b
000000
474747
ececec

```html
<!DOCTYPE html>
<html lang="en">
<head>
<meta charset="utf-8">
<title>Brasko Construction Business Card</title>
<link rel="stylesheet" href="https://fonts.googleapis.com/css2?family=Questrial&display=swap">
<style>
  :root {
    --page-bg: #d9d9d9;
    --card-light: #ffffff;
    --card-light-edge: #ececec;
    --card-dark: #1b1b1b;
    --card-black: #000000;
    --ink-dark: #000000;
    --ink-mid: #474747;
    --ink-light: #ececec;
    --accent: #00a990;
  }
  * { box-sizing: border-box; margin: 0; padding: 0; }
  html, body {
    width: 1200px;
    height: 900px;
    overflow: hidden;
    background: var(--page-bg);
    font-family: "Questrial", "Century Gothic", sans-serif;
  }
  .canvas {
    position: relative;
    width: 1200px;
    height: 900px;
  }
  .card {
    position: absolute;
    width: 700px;
    height: 400px;
    border-radius: 22px;
    overflow: hidden;
    box-shadow: 0 14px 30px rgba(0,0,0,0.25);
  }

  /* Front card */
  .card-front {
    left: 130px;
    top: 40px;
    background: linear-gradient(160deg, var(--card-light) 55%, var(--card-light-edge));
  }
  .machinery-illustration {
    position: absolute;
    left: 60px;
    top: 30px;
    width: 560px;
    height: 250px;
    border-radius: 60px;
    background: radial-gradient(ellipse at center, #f1f1f1 0%, #f7f7f7 55%, rgba(255,255,255,0) 80%);
  }
  .front-brand {
    position: absolute;
    left: 0;
    right: 0;
    top: 110px;
    display: flex;
    flex-direction: column;
    align-items: center;
    color: var(--ink-dark);
  }
  .front-brand .brand-row {
    display: flex;
    align-items: center;
    gap: 16px;
  }
  .brand-square {
    width: 46px;
    height: 46px;
    background: var(--ink-dark);
  }
  .front-brand .brand-name {
    font-size: 72px;
    letter-spacing: 6px;
    line-height: 1;
  }
  .front-brand .brand-sub {
    font-size: 30px;
    letter-spacing: 10px;
    margin-top: 6px;
  }
  .front-web {
    position: absolute;
    left: 0;
    right: 0;
    top: 300px;
    text-align: center;
    font-size: 17px;
    letter-spacing: 6px;
    color: var(--ink-mid);
  }
  .front-rule {
    position: absolute;
    left: 90px;
    right: 90px;
    top: 336px;
    height: 1px;
    background: var(--ink-mid);
    opacity: 0.6;
  }

  /* Back card */
  .card-back {
    left: 370px;
    top: 470px;
    background: linear-gradient(120deg, var(--card-black) 30%, var(--card-dark) 75%, #2a2a2a);
    color: var(--ink-light);
  }
  .back-brand {
    position: absolute;
    left: 40px;
    top: 150px;
    width: 330px;
    text-align: center;
  }
  .back-brand .brand-name {
    font-size: 60px;
    letter-spacing: 5px;
    line-height: 1;
  }
  .back-brand .brand-sub {
    font-size: 24px;
    letter-spacing: 7px;
    margin-top: 6px;
  }
  .back-divider {
    position: absolute;
    left: 395px;
    top: 40px;
    width: 1px;
    height: 300px;
    background: var(--ink-light);
    opacity: 0.7;
  }
  .contact {
    position: absolute;
    left: 418px;
    top: 44px;
    width: 270px;
  }
  .contact .person-name {
    font-size: 22px;
    letter-spacing: 1px;
  }
  .contact .person-role {
    font-size: 15px;
    margin-top: 4px;
  }
  .contact .address {
    font-size: 15px;
    line-height: 1.35;
    margin-top: 14px;
  }
  .contact-list {
    list-style: none;
    margin-top: 14px;
  }
  .contact-list li {
    display: flex;
    align-items: center;
    gap: 10px;
    font-size: 15px;
    line-height: 1.6;
  }
  .contact-list svg {
    width: 16px;
    height: 16px;
    flex: none;
  }
</style>
</head>
<body>
<div class="canvas">

  <section class="card card-front" aria-label="Business card front">
    <div class="machinery-illustration" role="img" aria-label="Faint illustration of construction machinery behind the logo"></div>
    <div class="front-brand">
      <div class="brand-row">
        <span class="brand-square"></span>
        <span class="brand-name">BRASKO</span>
      </div>
      <span class="brand-sub">CONSTRUCTION</span>
    </div>
    <p class="front-web">www.braskoconstruction.com</p>
    <div class="front-rule"></div>
  </section>

  <section class="card card-back" aria-label="Business card back">
    <div class="back-brand">
      <div class="brand-name">BRASKO</div>
      <div class="brand-sub">CONSTRUCTION</div>
    </div>
    <div class="back-divider"></div>
    <div class="contact">
      <p class="person-name">MARC LEFEVRE</p>
      <p class="person-role">Director</p>
      <p class="address">Maison Verte<br>12 rue des Lilas France</p>
      <ul class="contact-list">
        <li>
          <svg viewBox="0 0 16 16" aria-hidden="true"><rect x="4" y="1" width="8" height="14" rx="1.5" fill="none" stroke="currentColor" stroke-width="1.4"/><rect x="5.5" y="3" width="5" height="7" fill="currentColor"/><circle cx="8" cy="12.5" r="0.9" fill="currentColor"/></svg>
          +630-555-0148
        </li>
        <li>
          <svg viewBox="0 0 16 16" aria-hidden="true"><path d="M2 6c0-2 2-3 6-3s6 1 6 3v1h-3V5.5H5V7H2z" fill="currentColor"/><rect x="3" y="8" width="10" height="6" rx="1" fill="currentColor"/></svg>
          +630-555-0148
        </li>
        <li>
          <svg viewBox="0 0 16 16" aria-hidden="true"><rect x="1.5" y="3.5" width="13" height="9" rx="1" fill="currentColor"/><path d="M2 4.5l6 4.5 6-4.5" fill="none" stroke="#000" stroke-width="1.2"/></svg>
          marc@braskoconstruction.com
        </li>
        <li>
          <svg viewBox="0 0 16 16" aria-hidden="true"><circle cx="8" cy="8" r="6.3" fill="none" stroke="currentColor" stroke-width="1.4"/><ellipse cx="8" cy="8" rx="2.6" ry="6.3" fill="none" stroke="currentColor" stroke-width="1.1"/><path d="M1.8 8h12.4" stroke="currentColor" stroke-width="1.1"/></svg>
          www.braskoconstruction.com
        </li>
      </ul>
    </div>
  </section>

</div>
</body>
</html>
```